Decorative concrete business needs new business cards

Our company attracts homeowners and business with disposable cash. We are a artistic decorative coatings company that will transform your driveway, patio, floors or counter tops into a work of art. We also engrave logos and designs right into the concrete! We are upscale and very professional company. I am open for rearranging our logo on the business card and also to different color patterns. We like the blue and black as in Marlowbeck's logo. We also like blue and orange/yellow.

Target Market(s)

Adults 30-70

Industry/Entity Type

Concrete

Contact Information for Business Card

Simple: Name, phone, email, website and social media icons

Font styles to use
Serif

Colors

Designer to choose colors to be used in the design.

Requirements
Must have
• Must present a professional upscale appearance. I have attached before and after photos that show you what our industry does. Maybe I will have before and after photo on back of card.
Nice to have
• Artistic, but bold. Nothing whimsical or cute.
Should not have
• Should not have cartoon or childlike appearance.

```html
<!DOCTYPE html>
<html lang="en">
<head>
<meta charset="utf-8">
<title>Stoneleaf Finish Works — Business Card</title>
<link href="https://fonts.googleapis.com/css2?family=Cinzel:wght@400;600&family=Open+Sans:wght@400&display=swap" rel="stylesheet">
<style>
  :root {
    --page: #ececec;
    --card-white: #ffffff;
    --brand-blue: #1a74b8;
    --back-blue: #1b72b5;
    --ink: #222222;
    --faint-blue: #e6ecf6;
    --faint-grey: #e2e2e2;
  }
  html, body {
    margin: 0; padding: 0;
    width: 1200px; height: 1000px;
    overflow: hidden;
    background: var(--page);
  }
  .canvas { position: relative; width: 1200px; height: 1000px; }
  .card {
    position: absolute;
    left: 266px; width: 666px; height: 397px;
    box-shadow: 0 2px 8px rgba(0,0,0,0.18);
    overflow: hidden;
  }
  .card-front { top: 74px; background: var(--card-white); }
  .card-back { top: 534px; background: var(--back-blue); }

  .holder-name {
    position: absolute; left: 33px; top: 64px; margin: 0;
    font: 400 23px/1 "Cinzel", serif;
    color: var(--brand-blue); letter-spacing: 0.5px;
  }
  .holder-role {
    position: absolute; left: 33px; top: 95px; margin: 0;
    font: 400 16px/1 "Open Sans", sans-serif; color: var(--ink);
  }
  .address {
    position: absolute; left: 33px; top: 188px; margin: 0;
    font: 400 16px/25px "Open Sans", sans-serif; color: var(--ink); font-style: normal;
  }
  .contact-list {
    position: absolute; left: 33px; top: 256px; margin: 0; padding: 0;
    list-style: none;
    font: 400 16px/1 "Open Sans", sans-serif; color: var(--ink);
  }
  .contact-list li { display: flex; align-items: center; height: 25px; }
  .contact-list svg { width: 14px; height: 14px; margin-right: 7px; fill: var(--brand-blue); }
  .social {
    position: absolute; left: 33px; top: 345px;
    display: flex; align-items: center;
    font: 400 16px/1 "Open Sans", sans-serif; color: var(--ink);
  }
  .social-dot {
    width: 18px; height: 18px; border-radius: 50%;
    background: var(--brand-blue); margin-right: 6px;
  }
  .social-handle { margin-left: 7px; }

  .brand-mark {
    position: absolute; left: 356px; top: 44px;
    display: flex; align-items: center;
  }
  .brand-square { width: 76px; height: 76px; background: var(--brand-blue); margin-right: 12px; }
  .brand-name {
    font: 400 26px/28px "Cinzel", serif; color: var(--brand-blue);
    letter-spacing: 1px;
  }
  .brand-faint {
    position: absolute; left: 354px; top: 158px; width: 280px; height: 239px;
    background: linear-gradient(180deg, var(--faint-blue) 0%, var(--faint-grey) 100%);
  }

  .back-pattern { position: absolute; inset: 0; background: var(--back-blue); }
  .back-name {
    position: absolute; left: 0; right: 0; top: 130px; margin: 0;
    text-align: center;
    font: 400 48px/52px "Cinzel", serif; color: #ffffff; letter-spacing: 2px;
  }
  .back-name span { display: block; }
  .back-name .line-2 { font-size: 38px; line-height: 40px; }
  .back-name .line-3 { font-size: 36px; line-height: 40px; letter-spacing: 10px; }
</style>
</head>
<body>
<main class="canvas">
  <section class="card card-front" aria-label="Card front">
    <h1 class="holder-name">DORIAN HALVEK</h1>
    <p class="holder-role">Managing Director</p>
    <address class="address">1820 North Alder Lane<br>Westbury, MD 21990</address>
    <ul class="contact-list">
      <li><svg viewBox="0 0 16 16"><path d="M3 2h3l1 4-2 1c1 2 2 3 4 4l1-2 4 1v3c0 1-1 1-1 1C7 14 2 9 2 3c0 0 0-1 1-1z"/></svg>+ 000 000 0000</li>
      <li><svg viewBox="0 0 16 16"><path d="M1 3h14v10H1z M2 4l6 5 6-5" stroke="#fff" stroke-width="1"/></svg>info@stoneleaffinish.com</li>
      <li><svg viewBox="0 0 16 16"><circle cx="8" cy="8" r="7"/><path d="M1 8h14M8 1c-3 4-3 10 0 14M8 1c3 4 3 10 0 14" stroke="#fff" fill="none"/></svg>www.stoneleaffinish.com</li>
    </ul>
    <div class="social">
      <span class="social-dot"></span><span class="social-dot"></span><span class="social-dot"></span>
      <span class="social-handle">@stoneleaffinishwork</span>
    </div>
    <div class="brand-mark">
      <div class="brand-square"></div>
      <div class="brand-name">STONELEAF<br>FINISH<br>WORKS</div>
    </div>
    <div class="brand-faint" role="img" aria-label="Faint oversized brand symbol decoration"></div>
  </section>

  <section class="card card-back" aria-label="Card back">
    <div class="back-pattern" role="img" aria-label="Repeating brand symbol pattern in lighter blue"></div>
    <h2 class="back-name">
      <span class="line-1">STONELEAF</span>
      <span class="line-2">FINISH</span>
      <span class="line-3">WORKS</span>
    </h2>
  </section>
</main>
</body>
</html>
```